The Hearth Guard Desk needs a Wordpress site for Home, Life and Safety Emergencies

NEED CUSTOM THEME FILES FOR WORDPRESS ncluded. I need a wordpress website that I will be able to edit down the road. Content wise the site I was trying to build is accurate. http://www.hearthguarddesk-example.com The site focuses on life, safety and home emergencies. My target audience is the first time home buyer. Usually in mid 20's think engineering type person.

I am up for a complete redesign. I want it to look clean and neat.

Things I need to have on the site :

- 2 Menus - A main menu and a secondary menu at top of page
- Search Bar in one of the main menus
- Social Media Share Buttons on one of the menus
- I am up for a color change (Maybe something a little softer) Need Help
- Main Page should be set up as a main page with separate blog page
- Need a CTA / Sign up for newsletter on page (location can vary)
- Blog Categories: When clicked need to show the full article and image.
- If you click on my home safety you will see how they are set up as a grid. I do not like this I want them to be easy to read and flow in order.

The site is going to mainly provide information for First Time Home Buyers. Eventually a page will be set up to sign up for a paid Home Safety Course. For now I want to focus on the content.

Mail should function with mail chimp for now.
This needs to be a functioning theme that I can edit. I currently have the rights to divi builder if that helps. I don't want to have to worry about the site I just want to focus on content creation.

Thank you

Target Market(s)

First Time Home Buyers Usually person in their 20's or 30's. Someone of the engineering, legal aid type mindset.

Industry/Entity Type

Safety

Coding

Coded - Design and coding required

Font styles to use
Serif
Sans Serif
Script

Colors

Designer to choose colors to be used in the design.

Requirements
Must have
• Wordpress integration.
• 2 Menus on top - Main and secondary
• Search function in a menu
• Social Media Icons in menu
• Sidebar with image of myself and some info on top , posts , categories
• Categories of blog posts need to list on the page. Not grid.
• Email signup on page at some part. (can be bottom, top or side. )
• Nice Clean state Front page.
• Color Combination that works well. (Doesn't have to be what is their now)
• Current links to site.
• Pulse Basics needs to be a link to an external site ( http://www.pulseclassroomharbor-example.com)
Nice to have
• I am flexible on the main page site design. I am not good at this so anything you feel. I cannot describe what I want but I will know it when I see it.
• I will come up with the information. Of course if any copy could be provided and shows value I would be willing to pay extra.
Should not have
• Grid Style for blog posts.
• Blog Posts should be in list style and each post for each category will just go down the page by order of date posted.

```html
<!DOCTYPE html>
<html lang="en">
<head>
<meta charset="utf-8">
<title>The Hearth Guard Desk</title>
<link href="https://fonts.googleapis.com/css2?family=Open+Sans:ital,wght@0,400;0,600;0,700;1,400;1,600&display=swap" rel="stylesheet">
<style>
:root{
  --red:#ee2224;
  --brown:#6b3f22;
  --ink:#333333;
  --muted:#555555;
  --grey-bar:#efefef;
  --white:#ffffff;
  --icon-grey:#b4b4b4;
  --soc-1:#1d5aa8;
  --soc-2:#1aa6e0;
  --soc-3:#c9151e;
  --soc-4:#c2621c;
}
*{margin:0;padding:0;box-sizing:border-box}
html,body{width:1200px;height:2639px;overflow:hidden;background:var(--white)}
body{font-family:'Open Sans',Arial,sans-serif;color:var(--ink);position:relative}
a{color:inherit;text-decoration:none}

/* top bar */
.topbar{position:absolute;left:0;top:0;width:1200px;height:46px;background:var(--grey-bar)}
.secondary-menu{position:absolute;left:132px;top:0;display:flex;gap:34px;font-size:13.5px;line-height:46px;color:var(--ink)}
.top-social{position:absolute;left:920px;top:0;display:flex;gap:20px;align-items:center;height:46px}
.top-social span{width:10px;height:10px;background:#555;display:block}
.top-search{position:absolute;left:1052px;top:0;width:50px;height:46px;background:#dcdcdc;display:flex;align-items:center;justify-content:center}

/* header */
.header{position:absolute;left:0;top:46px;width:1200px;height:109px;background:var(--white)}
.brand{position:absolute;left:120px;top:30px;display:flex;align-items:center;gap:10px}
.brand-mark{width:22px;height:22px;background:var(--red)}
.brand-name{font-size:22px;font-weight:700;color:var(--red);line-height:1.1;width:150px}
.main-menu{position:absolute;right:96px;top:0;display:flex;gap:28px;font-size:13.5px;height:109px;align-items:center}
.main-menu a{position:relative;height:109px;display:flex;align-items:center;color:var(--ink)}
.main-menu a.active{color:var(--red)}
.main-menu a.active::after{content:"";position:absolute;left:0;right:0;bottom:-2px;height:4px;background:var(--red)}

/* hero */
.hero-photo{position:absolute;left:0;top:155px;width:1200px;height:620px;background:linear-gradient(180deg,#e9e4df 0%,#dcd3cb 45%,#efeceb 80%,#ffffff 100%)}
.hero-title{position:absolute;left:0;width:1200px;top:620px;text-align:center;font-size:47px;font-weight:700;color:var(--red)}
.hero-sub{position:absolute;left:0;width:1200px;top:680px;text-align:center;font-size:19px;letter-spacing:2px;color:var(--brown)}
.hero-prev{position:absolute;left:562px;top:742px;width:35px;height:36px;display:flex;align-items:center;justify-content:center}
.hero-next{position:absolute;left:602px;top:742px;width:35px;height:36px;background:var(--brown);display:flex;align-items:center;justify-content:center}

/* intro */
.intro-title{position:absolute;left:132px;top:803px;width:520px;font-size:20.5px;font-weight:700;line-height:28px;color:var(--ink)}
.intro-list{position:absolute;left:132px;top:898px;width:450px;list-style:none;font-size:13px;line-height:30px;color:var(--ink)}
.intro-list li{position:relative;padding-left:28px}
.intro-list li::before{content:"\2192";position:absolute;left:0;top:0;font-size:14px}
.btn-grey{position:absolute;left:141px;top:1197px;width:169px;height:38px;background:linear-gradient(#cfcfcf,#a9a9a9);color:var(--white);font-size:14px;font-weight:700;display:flex;align-items:center;justify-content:center}
.intro-photo{position:absolute;left:655px;top:804px;width:408px;height:407px;background:linear-gradient(135deg,#7fd0cf 0%,#c8d6dc 45%,#b88a64 100%)}
.intro-photo::after{content:"";position:absolute;left:14px;top:14px;right:14px;bottom:14px;border:1px solid rgba(255,255,255,.8)}

/* features */
.section-title{position:absolute;left:0;width:1200px;text-align:center;font-size:23px;font-weight:700;color:var(--ink)}
.feature{position:absolute;top:1334px;width:160px;text-align:center}
.feature-circle{width:130px;height:130px;border-radius:50%;background:var(--red);margin:0 auto;display:flex;align-items:center;justify-content:center}
.feature-circle.alt{background:var(--icon-grey)}
.feature-label{margin-top:14px;font-size:16.5px;font-weight:700;color:var(--ink)}

/* newsletter */
.newsletter{position:absolute;left:0;top:1554px;width:1200px;height:336px;background:var(--red)}
.nl-badge{position:absolute;left:159px;top:44px;width:130px;height:130px;border-radius:50%;background:var(--brown);display:flex;align-items:center;justify-content:center}
.nl-title{position:absolute;left:296px;top:52px;font-size:28px;font-weight:600;color:var(--white)}
.nl-text{position:absolute;left:296px;top:98px;width:740px;font-size:15px;line-height:32px;color:var(--white)}
.nl-input{position:absolute;top:211px;height:44px;background:var(--white);font-size:12px;color:#999;padding-left:16px;display:flex;align-items:center;letter-spacing:.5px}
.nl-submit{position:absolute;left:824px;top:211px;width:185px;height:44px;background:linear-gradient(#c9c9c9,#a5a5a5);color:var(--white);font-size:19px;font-weight:700;display:flex;align-items:center;justify-content:center}

/* blog */
.post-date{position:absolute;left:150px;top:2015px;width:80px;text-align:center;color:var(--red);font-weight:700}
.post-day{font-size:32px;line-height:38px}
.post-month{font-size:24px;line-height:30px}
.post-year{font-size:13px;color:var(--ink);line-height:20px}
.post-photo{position:absolute;left:238px;top:2006px;width:322px;height:229px;background:linear-gradient(135deg,#e6e1da 0%,#9aa3ab 45%,#2f4a6b 100%)}
.post-title{position:absolute;left:595px;top:2042px;width:420px;font-size:23px;font-weight:700;line-height:29px;color:var(--ink)}
.post-author{position:absolute;left:600px;top:2112px;font-size:13px;font-style:italic;font-weight:600;color:var(--red);display:flex;align-items:center;gap:10px}
.post-excerpt{position:absolute;left:600px;top:2141px;width:440px;font-size:12px;line-height:22px;color:var(--ink)}
.dots{position:absolute;left:568px;top:2269px;display:flex;gap:8px;align-items:center}
.dots span{width:8px;height:8px;border-radius:50%;background:#777}
.dots span.on{width:13px;height:13px;background:none;border:1px solid #777}

/* footer */
.footer{position:absolute;left:0;top:2320px;width:1200px;height:285px;background:var(--grey-bar)}
.f-head{position:absolute;top:22px;font-size:20px;font-weight:400;color:var(--ink)}
.f-links{position:absolute;left:137px;top:66px;list-style:none;font-size:12px;line-height:26px}
.f-links li::before{content:"\203A";margin-right:12px}
.testimonial{position:absolute;left:336px;top:60px;width:217px;height:128px;background:#dcdcdc;border-radius:8px;padding:14px;font-size:11.5px;line-height:19px;color:var(--muted);text-align:justify}
.testimonial::after{content:"";position:absolute;left:22px;bottom:-12px;border-left:12px solid #dcdcdc;border-bottom:12px solid transparent}
.t-avatar{position:absolute;left:369px;top:200px;width:44px;height:44px;border-radius:50%;background:linear-gradient(#8b5a3c,#3a2a22)}
.t-name{position:absolute;left:430px;top:206px;font-size:13.5px;line-height:18px;color:var(--red)}
.contact{position:absolute;left:627px;top:66px;font-size:12px;line-height:20px}
.contact div{display:flex;gap:14px;margin-bottom:16px;align-items:flex-start}
.contact svg{flex:none;margin-top:3px}
.social-list{position:absolute;left:894px;top:62px;font-size:12px}
.social-list div{display:flex;align-items:center;gap:14px;height:38px}
.social-list span{width:26px;height:26px;display:block}
.bottombar{position:absolute;left:0;top:2605px;width:1200px;height:34px;background:#dedede;text-align:center;font-size:11.5px;line-height:34px;color:var(--ink)}
</style>
</head>
<body>

<div class="topbar">
  <nav class="secondary-menu"><a href="#">Home Safety</a><a href="#">Life Safety</a><a href="#">Fire Safety</a><a href="#">Pet Safety</a><a href="#">Safety Saturday</a></nav>
  <div class="top-social" aria-label="Social links"><span></span><span></span><span></span><span></span></div>
  <div class="top-search">
    <svg width="16" height="16" viewBox="0 0 16 16"><circle cx="6.5" cy="6.5" r="5" fill="none" stroke="#444" stroke-width="2"/><line x1="10.5" y1="10.5" x2="15" y2="15" stroke="#444" stroke-width="2.2"/></svg>
  </div>
</div>

<header class="header">
  <a class="brand" href="#"><span class="brand-mark"></span><span class="brand-name">The Hearth Guard Desk</span></a>
  <nav class="main-menu">
    <a class="active" href="#">HOME</a><a href="#">ABOUT ME</a><a href="#">SAFETY INFO</a><a href="http://www.pulseclassroomharbor-example.com">PULSE BASICS</a><a href="#">PREVENT HOME DISASTERS</a><a href="#">CONTACT ME</a>
  </nav>
</header>

<div class="hero-photo" role="img" aria-label="Smiling young family with two children relaxing together on a bed in a bright room"></div>
<h1 class="hero-title">THE HEARTH GUARD DESK</h1>
<p class="hero-sub">KNOW SAFETY. DISASTER NEVER SLEEPS</p>
<div class="hero-prev"><svg width="12" height="18" viewBox="0 0 12 18"><polyline points="10,2 3,9 10,16" fill="none" stroke="#444" stroke-width="2"/></svg></div>
<div class="hero-next"><svg width="12" height="18" viewBox="0 0 12 18"><polyline points="2,2 9,9 2,16" fill="none" stroke="#fff" stroke-width="2"/></svg></div>

<h2 class="intro-title">WANT TO PROTECT YOUR HOME OR LOVED ONE FROM AN EMERGENCY ? HAVE YOU HAD A HOME EMERGENCY ? NOT SURE WHAT TO DO ?</h2>
<ul class="intro-list">
  <li>House Fires Kill 8 People every day.</li>
  <li>Flood damage accounts for $14.3 Billion in Property Damage Yearly.</li>
  <li>Disaster Never Sleeps and Always strikes at the Worst possible time.</li>
  <li>Be Prepared. Know What to do.</li>
  <li>I am here for you.</li>
  <li>As an Emergency Services Professional I want to share what I have seen and how to Help.</li>
  <li>We all have busy lives. Preparing &nbsp;NOW will Save you Time, Money and could Save A Life.</li>
</ul>
<a class="btn-grey" href="#">SAFETY MEASURES</a>
<div class="intro-photo" role="img" aria-label="Couple reviewing a tablet with a safety advisor"></div>

<h2 class="section-title" style="top:1259px">OUR FEATURES</h2>

<div class="feature" style="left:84px"><div class="feature-circle">
  <svg width="64" height="70" viewBox="0 0 64 70" fill="none" stroke="#fff" stroke-width="4"><circle cx="32" cy="20" r="15"/><path d="M6 66c0-16 12-26 26-26s26 10 26 26z"/></svg>
</div><div class="feature-label">ABOUT ME</div></div>

<div class="feature" style="left:258px"><div class="feature-circle">
  <svg width="76" height="70" viewBox="0 0 76 70" fill="#fff"><path d="M38 6 16 26h6v18h32V26h6z"/><path d="M4 44c8 0 14 8 18 14h32c4-6 10-14 18-14v8c-6 0-10 8-14 14H18C14 60 10 52 4 52z"/></svg>
</div><div class="feature-label">HOME SAFETY</div></div>

<div class="feature" style="left:432px"><div class="feature-circle alt">
  <svg width="76" height="70" viewBox="0 0 76 70" fill="#fff"><circle cx="28" cy="16" r="8"/><circle cx="48" cy="16" r="8"/><circle cx="38" cy="34" r="6"/><path d="M16 42c0-10 6-16 12-16s10 4 10 4 4-4 10-4 12 6 12 16z"/><path d="M4 44c8 0 14 8 18 14h32c4-6 10-14 18-14v8c-6 0-10 8-14 14H18C14 60 10 52 4 52z"/></svg>
</div><div class="feature-label">LIFE SAFETY</div></div>

<div class="feature" style="left:608px"><div class="feature-circle">
  <svg width="76" height="70" viewBox="0 0 76 70" fill="#fff"><circle cx="40" cy="18" r="9" fill="none" stroke="#fff" stroke-width="5" stroke-dasharray="4 3"/><circle cx="56" cy="30" r="6" fill="none" stroke="#fff" stroke-width="4" stroke-dasharray="3 2"/><path d="M4 46c10 0 18 6 24 6h18c4 0 4 6 0 6H30v2h20l18-10c4-2 6 4 2 6L50 66H22L4 58z"/></svg>
</div><div class="feature-label">RESOURCES</div></div>

<div class="feature" style="left:782px"><div class="feature-circle">
  <svg width="76" height="70" viewBox="0 0 76 70" fill="none" stroke="#fff" stroke-width="5"><path d="M8 34 38 8l30 26"/><path d="M16 30v32h44V30"/><circle cx="32" cy="44" r="5" fill="#fff" stroke="none"/><path d="M38 60c0-8 4-14 10-14s8 6 8 14z" fill="#fff" stroke="none"/></svg>
</div><div class="feature-label">PET SAFETY</div></div>

<div class="feature" style="left:957px"><div class="feature-circle">
  <svg width="76" height="70" viewBox="0 0 76 70" fill="#fff"><path d="M26 6c4 12 18 16 18 34 0 12-8 22-18 22S8 52 8 40c0-10 8-14 8-22 6 4 6 10 6 10 4-6 4-14 4-22z"/><rect x="44" y="36" width="26" height="22" rx="2"/><path d="M49 36v-8a8 8 0 0 1 16 0v8" fill="none" stroke="#fff" stroke-width="4"/></svg>
</div><div class="feature-label">FIRE SAFETY</div></div>

<section class="newsletter">
  <div class="nl-badge"><svg width="50" height="36" viewBox="0 0 50 36" fill="none" stroke="#fff" stroke-width="2.5"><rect x="2" y="2" width="46" height="32"/><polyline points="2,2 25,20 48,2"/></svg></div>
  <h2 class="nl-title">SIGN UP FOR OUR NEWSLETTER</h2>
  <p class="nl-text">Life gets busy. Don't worry about having to check the site daily. Though, I would love it. Sign up today to receive a weekly update. This information will help in an emergency but can save you money and time too. Don't miss out. Sign Up Today !</p>
  <div class="nl-input" style="left:294px;width:253px">ENTER YOUR NAME</div>
  <div class="nl-input" style="left:558px;width:253px">ENTER YOUR EMAIL</div>
  <div class="nl-submit">SUBSCRIBE</div>
</section>

<h2 class="section-title" style="top:1928px">BLOG</h2>
<div class="post-date"><div class="post-day">03</div><div class="post-month">JAN</div><div class="post-year">2017</div></div>
<div class="post-photo" role="img" aria-label="Advisor shaking hands with an older couple at a home consultation"></div>
<h3 class="post-title">SED UT PERSPICIATIS UNDE OMNIS ISTE NATUS ERROR SIT</h3>
<div class="post-author"><svg width="12" height="13" viewBox="0 0 12 13" fill="none" stroke="#ee2224" stroke-width="1.5"><circle cx="6" cy="4" r="3"/><path d="M1 12c0-3 2-5 5-5s5 2 5 5z"/></svg>by Mara Ellison</div>
<p class="post-excerpt">Nemo enim ipsam voluptatem quia voluptas sit aspernatur aut odit aut fugit, sed quia consequuntur magni dolores eos qui ratione voluptatem</p>
<div class="dots"><span></span><span class="on"></span><span></span><span></span></div>

<footer class="footer">
  <h4 class="f-head" style="left:137px">Quick Links</h4>
  <ul class="f-links"><li>Home</li><li>About Us</li><li>Safety Info</li><li>Pulse Basics</li><li>Prevent Home Disasters</li><li>Contact Me</li></ul>

  <h4 class="f-head" style="left:341px">Testimonials</h4>
  <div class="testimonial">“Lorem ipsum dolor sit amet, consectetur adipiscing elit, sed do eiusmod tempor incididunt ut labore et dolore magna aliqua. Ut enim ad minim veniam.”</div>
  <div class="t-avatar" role="img" aria-label="Reviewer portrait"></div>
  <div class="t-name">Owen Tarrow,<br>Lorium ipsum</div>

  <h4 class="f-head" style="left:627px">Contact Us</h4>
  <div class="contact">
    <div><svg width="11" height="15" viewBox="0 0 11 15"><path d="M5.5 0A5.5 5.5 0 0 0 0 5.5C0 10 5.5 15 5.5 15S11 10 11 5.5A5.5 5.5 0 0 0 5.5 0z" fill="#222"/><circle cx="5.5" cy="5.5" r="2" fill="#efefef"/></svg><span>Main Office 4820 Alder Crest Rd<br>North Bayfield</span></div>
    <div><svg width="12" height="12" viewBox="0 0 12 12"><path d="M2 0l3 3-1.5 2a7 7 0 0 0 3.5 3.5L9 7l3 3-2 2C5 12 0 7 0 2z" fill="#222"/></svg><span>(555)-012-4738</span></div>
    <div><svg width="12" height="10" viewBox="0 0 12 10"><rect width="12" height="10" fill="#222"/><polyline points="0,0 6,5 12,0" fill="none" stroke="#efefef" stroke-width="1.2"/></svg><span>hello@hearthguarddesk-example.com</span></div>
  </div>

  <h4 class="f-head" style="left:894px">Follow Us</h4>
  <div class="social-list">
    <div><span style="background:var(--soc-1)"></span>Friendwall</div>
    <div><span style="background:var(--soc-2)"></span>Chirpline</div>
    <div><span style="background:var(--soc-3)"></span>Pinboardly</div>
    <div><span style="background:var(--soc-4)"></span>Snapframe</div>
  </div>
</footer>
<div class="bottombar">Copyrights © 2017 - All Rights Reserved</div>

</body>
</html>
```